Luxury Caviar Tin Label for High End Caviar Retailer

We are looking for a new caviar label design. We want something unique, preferably black and gold or dark blue and gold. We want a modern and luxurious feel. We have several types of caviar so we need to be able to change the name of the caviar when we print the labels. See inspiration attached. Logo is also attached. More about us: velmoronfare.com

Industry/Entity Type

fine foods industry, caviar

Font styles to use
Serif
Decorative

Requirements
Must have
• KT Velmoron Logo, space for caviar name
Nice to have
• black and gold, blue and gold

```html
<!DOCTYPE html>
<html lang="en">
<head>
<meta charset="utf-8">
<title>KT Velmoron – Osetra Imperial Gold Label</title>
<link href="https://fonts.googleapis.com/css2?family=Marcellus&family=Pinyon+Script&family=Cinzel:wght@400;500;900&display=swap" rel="stylesheet">
<style>
  :root {
    --paper: #ffffff;
    --tin-black: #000000;
    --gold-deep: #6b3c12;
    --gold-mid: #b07a35;
    --gold-bright: #f3d58a;
    --gold-pale: #fff6e3;
    --gold-text: #b98a46;
    --gold-shine: linear-gradient(90deg, #7a4716 0%, #c58b44 22%, #fff5e4 40%, #a8692a 58%, #f4d48a 80%, #c99a4c 100%);
  }
  * { margin: 0; padding: 0; box-sizing: border-box; }
  html, body {
    width: 1200px;
    height: 1195px;
    overflow: hidden;
    background: var(--paper);
  }
  .label {
    position: relative;
    width: 1200px;
    height: 1195px;
  }
  .label-rings {
    position: absolute;
    inset: 0;
  }
  .crest {
    position: absolute;
    left: 274px;
    top: 252px;
    width: 647px;
    height: 326px;
    border-radius: 40% 40% 46% 46% / 30% 30% 60% 60%;
    background: radial-gradient(ellipse at 50% 45%, #1a0f05 0%, #1a0f05 28%, #8a5a24 36%, #d7ac5e 52%, #6a3d14 72%, rgba(0,0,0,0) 86%);
    opacity: .85;
  }
  .brand-name {
    position: absolute;
    left: 0;
    width: 1200px;
    top: 600px;
    text-align: center;
    font-family: "Marcellus", serif;
    font-size: 84px;
    line-height: 1;
    letter-spacing: 1px;
    color: var(--gold-text);
  }
  .shine {
    background: var(--gold-shine);
    -webkit-background-clip: text;
    background-clip: text;
    color: transparent;
  }
  .tagline {
    position: absolute;
    left: 0;
    width: 1200px;
    top: 690px;
    text-align: center;
    font-family: "Pinyon Script", cursive;
    font-size: 58px;
    line-height: 1.1;
  }
  .divider {
    position: absolute;
    left: 491px;
    top: 784px;
    width: 249px;
    height: 1px;
    background: linear-gradient(90deg, rgba(176,122,53,0), var(--gold-mid) 20%, var(--gold-bright) 50%, var(--gold-mid) 80%, rgba(176,122,53,0));
  }
  .variety {
    position: absolute;
    left: 0;
    width: 1200px;
    top: 802px;
    text-align: center;
    font-family: "Cinzel", serif;
    font-weight: 500;
    font-size: 40px;
    line-height: 1;
    letter-spacing: 15px;
    padding-left: 15px;
  }
  .variety .initial { font-size: 40px; }
  .variety .rest { font-size: 31px; }
  .grade {
    position: absolute;
    left: 0;
    width: 1200px;
    top: 848px;
    text-align: center;
    font-family: "Cinzel", serif;
    font-weight: 900;
    font-size: 60px;
    line-height: 1;
    letter-spacing: 4px;
  }
  .flourish {
    position: absolute;
    left: 566px;
    top: 936px;
    width: 94px;
    height: 46px;
    border-radius: 50%;
    background: radial-gradient(ellipse, #d7ac5e 0%, #8a5a24 55%, rgba(0,0,0,0) 75%);
  }
</style>
</head>
<body>
  <main class="label">
    <svg class="label-rings" width="1200" height="1195" viewBox="0 0 1200 1195" aria-hidden="true">
      <defs>
        <linearGradient id="ringGold" x1="0" y1="0" x2="1" y2="1">
          <stop offset="0" stop-color="#f3d58a"/>
          <stop offset=".35" stop-color="#8a5422"/>
          <stop offset=".6" stop-color="#fff1d6"/>
          <stop offset="1" stop-color="#b07a35"/>
        </linearGradient>
      </defs>
      <circle class="tin" cx="597" cy="597" r="517" fill="var(--tin-black)"/>
      <circle class="ring-line" cx="597" cy="597" r="479" fill="none" stroke="url(#ringGold)" stroke-width="1.6"/>
      <circle class="ring-dots" cx="597" cy="597" r="466" fill="none" stroke="url(#ringGold)" stroke-width="3" stroke-linecap="round" stroke-dasharray="0 9.3"/>
    </svg>

    <div class="crest" role="img" aria-label="Gold engraved heraldic crest with shield and acanthus scrollwork"></div>

    <h1 class="brand-name">KT VELMORON</h1>
    <p class="tagline shine">Premium Quality</p>
    <div class="divider"></div>
    <p class="variety shine"><span class="initial">O</span><span class="rest">SETRA</span> <span class="initial">I</span><span class="rest">MPERIAL</span></p>
    <p class="grade shine">GOLD</p>

    <div class="flourish" role="img" aria-label="Small gold leaf flourish ornament"></div>
  </main>
</body>
</html>
```